AUSTRALIAN CONSULTING FIRM BUSINESS CARD - MODERN

We are wanting a modern, clean lined business card design. We are professional niche consultancy firm situated in Australia called Harbrook Advisory Partners Pty Ltd.
The card should communicate professionalism and creativity and draw on our logo design (attached).
The design should be two sided, landscape orientation.
Target Market(s)
government, not for profit sector, corporate clients
Industry/Entity Type
Landscape
Requirements
Must have
- logo
no new introduced colours

```html
<!DOCTYPE html>
<html lang="en">
<head>
<meta charset="utf-8">
<title>Harbrook Advisory Partners – Business Card</title>
<link href="https://fonts.googleapis.com/css2?family=Arimo:wght@400;700&display=swap" rel="stylesheet">
<style>
  :root {
    --page: #ffffff;
    --card: #e8ebf4;
    --navy: #1f3f9a;
    --accent: #2aa6dc;
    --text: #2b3f8f;
  }
  html, body {
    margin: 0;
    width: 1200px;
    height: 900px;
    overflow: hidden;
    background: var(--page);
    font-family: "Arimo", Arial, sans-serif;
  }
  .canvas { position: relative; width: 1200px; height: 900px; }
  .card {
    position: absolute;
    width: 510px;
    height: 296px;
    background: var(--card);
    overflow: hidden;
  }
  .card--front { left: 70px; top: 270px; }
  .card--back { left: 620px; top: 274px; }

  .brand {
    position: absolute;
    display: flex;
    align-items: center;
    gap: 10px;
  }
  .brand__dot {
    width: 26px; height: 26px;
    border-radius: 50%;
    background: var(--accent);
    flex: none;
  }
  .brand__name {
    color: var(--navy);
    font-weight: 700;
    font-size: 19px;
    line-height: 1.1;
    text-transform: uppercase;
  }
  .card--front .brand { left: 130px; top: 88px; }
  .brand__reflection {
    position: absolute;
    left: 166px; top: 154px;
    color: var(--navy);
    font-weight: 700;
    font-size: 19px;
    line-height: 1.1;
    text-transform: uppercase;
    transform: scaleY(-1);
    opacity: 0.12;
  }
  .rule { position: absolute; background: var(--navy); height: 2px; }
  .card--front .rule { left: 130px; top: 150px; width: 244px; }

  .card--back .brand { left: 48px; top: 54px; }
  .card--back .brand__name { font-size: 17px; }
  .frame { position: absolute; left: 0; top: 0; }

  .person { position: absolute; left: 346px; top: 22px; color: var(--text); }
  .person__name { font-size: 17px; margin: 0; }
  .person__title { font-size: 11px; margin: 4px 0 0; }

  .contact {
    position: absolute;
    left: 346px; top: 172px;
    color: var(--text);
    font-size: 12px;
    line-height: 15px;
    margin: 0;
  }
  .contact__gap { display: block; height: 9px; }
</style>
</head>
<body>
<main class="canvas">
  <section class="card card--front" aria-label="Card front">
    <div class="brand">
      <span class="brand__dot"></span>
      <span class="brand__name">Harbrook Advisory<br>Partners Pty Ltd</span>
    </div>
    <div class="rule"></div>
    <div class="brand__reflection" aria-hidden="true">Harbrook Advisory<br>Partners Pty Ltd</div>
  </section>

  <section class="card card--back" aria-label="Card back">
    <div class="brand">
      <span class="brand__dot"></span>
      <span class="brand__name">Harbrook Advisory<br>Partners Pty Ltd</span>
    </div>
    <svg class="frame" width="510" height="296" viewBox="0 0 510 296" aria-hidden="true">
      <polyline points="46,130 320,130 320,264 484,264" fill="none" stroke="var(--navy)" stroke-width="2"/>
    </svg>
    <div class="person">
      <p class="person__name">Employee Name</p>
      <p class="person__title">Title</p>
    </div>
    <p class="contact">
      123 Street Address<br>
      Suite 456<br>
      City (Australia)<br>
      <span class="contact__gap"></span>
      T:123-456-7890<br>
      info@email.com
    </p>
  </section>
</main>
</body>
</html>
```